Custom Home Builder Website

We need a re-design of a website for our client: "http://www.dorvelbuildworks.com". Their current design is outdated and has flash. We need to make it responsive for all devices and with a more professional look.

Pages to consider:
1. Home page
2. Portfolio page - gallery of projects (multiple images of a project with captions, and a main text area for each project).

Good clean design reflecting quality craftsmanship is a must.

We only need designs, no coding required

Target Market(s)

The intended market is home owners looking to build with a reputable and professional home builder.

Industry/Entity Type

Home Builder

Requirements
Must have
• Must Have:
• - main areas of site: home, portfolio, video gallery, contact
Nice to have
• - Maybe pullquotes from testimonials placed as slideshow?

```html
<!DOCTYPE html>
<html lang="en">
<head>
<meta charset="utf-8">
<title>Dorvel Buildworks — Custom Homes</title>
<link href="https://fonts.googleapis.com/css2?family=Marcellus&family=Open+Sans:wght@300;400&display=swap" rel="stylesheet">
<style>
:root{
  --tan:#b8976a;
  --tan-dark:#a07c4c;
  --accent:#b7783a;
  --charcoal:#2f2f2d;
  --charcoal-deep:#232321;
  --nav:#333333;
  --text:#9a9a9a;
  --heading:#333;
  --paper:#ffffff;
  --footer-text:#a8a8a2;
}
*{margin:0;padding:0;box-sizing:border-box}
html,body{width:1086px;height:1200px;overflow:hidden;background:var(--paper)}
body{position:relative;font-family:Arial,Helvetica,sans-serif}
h1,h2,h3,h4{font-weight:normal}
.abs{position:absolute}
.hero{left:0;top:0;width:1086px;height:524px;background:linear-gradient(180deg,#cbc6bf 0%,#b8b1a7 50%,#948b7e 80%,#7c7466 100%)}
.callus{right:184px;top:13px;font-size:12px;font-weight:bold;color:#111}
.callus span{font-weight:normal;font-size:15px;color:#fff}
.brand{left:167px;top:38px;width:190px;height:59px;background:#fff;display:flex;align-items:center;padding-left:14px}
.brand-name{font-family:"Marcellus",serif;font-size:16px;color:var(--tan-dark);letter-spacing:.3px;white-space:nowrap}
.nav{left:333px;top:38px;width:584px;height:59px}
.nav ul{position:absolute;left:0;top:0;list-style:none;height:59px;width:584px}
.nav li{position:absolute;top:23px;font-size:12px;color:#fff;white-space:nowrap}
.tagline{left:181px;top:428px;font-family:"Open Sans",sans-serif;font-weight:300;font-size:40px;color:#fff;letter-spacing:.3px;white-space:nowrap}
.btn-learn{left:738px;top:439px}
.btn-label{position:absolute;font-size:12px;color:#fff;letter-spacing:.3px}
.card{left:150px;top:498px;width:786px;height:520px}
.section-title{font-family:"Marcellus",serif;font-size:15px;color:var(--heading);letter-spacing:.4px}
.strip{left:182px;top:563px}
.sub-title{font-family:"Open Sans",sans-serif;font-size:12px;color:var(--accent)}
.body-copy{left:183px;width:452px;font-size:9.6px;line-height:14px;color:var(--text);text-align:justify}
.news-title{left:677px;font-family:"Open Sans",sans-serif;font-size:12px;color:var(--accent);white-space:nowrap}
.news-title span{color:#333;letter-spacing:.6px}
.news-thumb{left:677px;width:44px;height:44px;background:linear-gradient(135deg,#6b5440,#a6876a 60%,#4a3a2c);border:1px solid #888}
.news-copy{left:728px;width:176px;font-size:9.6px;line-height:14px;color:var(--text)}
.news-rule{left:677px;width:226px;height:1px;background:linear-gradient(90deg,transparent,#e7e1d8,transparent)}
.field{left:677px;width:226px;height:28px;border:1px solid #e0d2b8;background:linear-gradient(180deg,#f5efe3,#fbf8f2);font-size:9.6px;color:#b59a70;padding:9px 7px}
.footer{left:0;top:1017px;width:1086px;height:138px;background:var(--charcoal);border-top:4px solid #d8c9b0}
.footer-bar{left:0;top:1155px;width:1086px;height:45px;background:var(--charcoal-deep);text-align:center;font-size:9.6px;color:var(--footer-text);padding-top:16px}
.footer-bar span{color:var(--tan)}
.f-head{top:1040px;font-family:"Marcellus",serif;font-size:15px;color:var(--tan);letter-spacing:.4px}
.f-links{top:1069px;list-style:none;font-size:9.6px;line-height:16.5px;color:var(--footer-text)}
.f-links .on{color:var(--tan)}
.map{left:790px;top:1060px;width:100px;height:80px;background:radial-gradient(ellipse,#3a3a37 0%,transparent 70%)}
.contact{left:731px;top:1069px;font-size:9.6px;color:var(--footer-text);line-height:11px}
.contact div{position:absolute;left:0;white-space:nowrap}
.contact svg{position:absolute;left:0;top:0}
.contact p{margin-left:14px}
</style>
</head>
<body>

<div class="abs hero" role="img" aria-label="Photo of a bright child's bedroom interior"></div>

<svg class="abs" style="left:140px;top:260px" width="32" height="52" viewBox="0 0 32 52" aria-hidden="true"><polyline points="26,3 5,26 26,49" fill="none" stroke="#fff" stroke-width="1.5"/></svg>
<svg class="abs" style="left:915px;top:260px" width="32" height="52" viewBox="0 0 32 52" aria-hidden="true"><polyline points="6,3 27,26 6,49" fill="none" stroke="#111" stroke-width="1.5"/></svg>

<div class="abs callus">CALL US ON : <span>(555) 310-2846</span></div>

<div class="abs brand"><span class="brand-name">Dorvel Buildworks</span></div>

<nav class="abs nav">
  <svg class="abs" style="left:0;top:0" width="584" height="59" viewBox="0 0 584 59" aria-hidden="true">
    <polygon points="0,0 584,0 584,59 24,59" fill="var(--nav)"/>
    <polygon points="62,0 134,0 158,59 86,59" fill="var(--tan)"/>
  </svg>
  <ul>
    <li style="left:26px">Home</li>
    <li style="left:89px">About Us</li>
    <li style="left:157px">Services</li>
    <li style="left:222px">Portfolio</li>
    <li style="left:284px">Video Gallery</li>
    <li style="left:372px">Dorvel Rewards</li>
    <li style="left:481px">News</li>
    <li style="left:531px">Contact</li>
  </ul>
</nav>

<div class="abs tagline">When You Want it Done Right</div>
<div class="abs btn-learn">
  <svg width="160" height="31" viewBox="0 0 160 31" aria-hidden="true">
    <rect x=".5" y=".5" width="159" height="30" fill="#2c2c2c" stroke="#777"/>
    <polygon points="112,1 159,1 159,30 124,30" fill="var(--tan)"/>
    <polyline points="139,9 145,15.5 139,22" fill="none" stroke="#222" stroke-width="1.3"/>
  </svg>
  <span class="btn-label" style="left:25px;top:10px">LEARN MORE</span>
</div>

<div class="abs card">
  <svg width="786" height="520" viewBox="0 0 786 520" aria-hidden="true">
    <defs>
      <linearGradient id="cardTop" x1="0" y1="0" x2="0" y2="1">
        <stop offset="0" stop-color="#e6dccb"/><stop offset=".18" stop-color="#fbf9f5"/><stop offset=".3" stop-color="#fff"/>
      </linearGradient>
    </defs>
    <polygon points="17,0 769,0 786,26 786,520 0,520 0,26" fill="url(#cardTop)"/>
    <line x1="506" y1="32" x2="506" y2="490" stroke="#ece7df"/>
  </svg>
</div>

<h2 class="abs section-title" style="left:184px;top:530px">PROJECT DETAILE</h2>

<div class="abs strip">
  <svg width="454" height="83" viewBox="0 0 454 83" role="img" aria-label="Project thumbnails: home exterior, wooded deck and bathroom interior">
    <rect x=".5" y=".5" width="453" height="82" fill="#222" stroke="#111"/>
    <polygon points="48,2 178,2 132,81 2,81 2,72" fill="#8f9294"/>
    <polygon points="180,2 318,2 272,81 134,81" fill="#5d6352"/>
    <polygon points="320,2 452,2 452,10 407,81 274,81" fill="#5b4a3c"/>
    <polygon points="2,2 46,2 2,76" fill="#2b2b2b"/>
    <polygon points="452,14 452,81 410,81" fill="var(--tan)"/>
    <polyline points="21,11 16,16 21,21" fill="none" stroke="#fff" stroke-width="2.4"/>
    <polyline points="432,61 437,66 432,71" fill="none" stroke="#fff" stroke-width="2.4"/>
  </svg>
</div>

<h3 class="abs sub-title" style="left:183px;top:657px">Custom Homes</h3>

<p class="abs body-copy" style="top:682px">Lorem ipsum dolor sit amet, consectetur adipiscing elit. Proin sit amet dui velit. Class aptent taciti sociosqu ad litora torquent per conubia nostra, per inceptos himenaeos. Etiam nisl massa, pharetra in imperdiet iaculis, vehicula eget leo. Nunc dictum lectus ac metus consequat vulputate. Proin ultrices lacus sed aliquam tincidunt. Fusce pellentesque arcu quis libero iaculis varius. Nunc nec diam augue. Etiam im perdiet porttitor nisi, sit amet cursus urna lobortis et. Phasellus non nibh diam. Curabitur vulputate libero pretium velit auctor tincidunt. Sed venenatis, orci feugiat sagittis lobortis, est lectus iaculis massa, quis egestas risus ligula sit amet purus.</p>
<p class="abs body-copy" style="top:790px">Donec iaculis euismod semper. Maecenas aliquet viverra tempor. In non tristique quam.</p>
<p class="abs body-copy" style="top:814px">Maecenas sollicitudin faucibus nulla, at auctor nisi condimentum ut. Aliquam egestas consequat erat, nec ultrices lacus ullamcorper non. Nullam id tellus luctus, eleifend magna eu, viverra nisl. Phasellus gravida ipsum sit amet nibh ultricies, ut consequat leo feugiat. Proin lacus sem, malesuada vel nisi sed, molestie tempus libero. Sed fringilla lectus ultrices, accumsan tellus nec, semper arcu. Quisque consequat massa ac elementum molestie. Nunc hendrerit sodales justo, ac gravida libero. Etiam eu sodales urna.</p>
<p class="abs body-copy" style="top:896px">Sed pretium mi commodo pharetra congue. Integer quam nisl, mattis sed interdum in, sollicitudin vel est. Donec eu dignissim nisl. Nunc dignissim elit sit amet leo bibendum, egestas auctor justo fringilla. Donec gravida metus a imperdiet consectetur. Donec sit amet mi nec metus dictum ornare. Sed volutpat, sem vitae interdum bibendum, elit ante mattis massa, non adipiscing sapien felis consequat est. Aenean quis nisl in justo tincidunt sagittis sed vel arcu.</p>

<h2 class="abs section-title" style="left:677px;top:530px">OUR NEWS!</h2>

<h3 class="abs news-title" style="top:557px">Phasellus in nunc purus <span>JUNE 28, 2013</span></h3>
<div class="abs news-thumb" style="top:580px" role="img" aria-label="Interior room thumbnail"></div>
<p class="abs news-copy" style="top:581px">Morbi vel metus vitae mi aliquam interdu sed eleifend quam. Sed sed ultrices erat. Sed tincidunt bibendum sollicitudin.</p>
<div class="abs news-rule" style="top:636px"></div>

<h3 class="abs news-title" style="top:643px">Phasellus in nunc purus <span>JUNE 28, 2013</span></h3>
<div class="abs news-thumb" style="top:666px" role="img" aria-label="Interior room thumbnail"></div>
<p class="abs news-copy" style="top:667px">Morbi vel metus vitae mi aliquam interdu sed eleifend quam. Sed sed ultrices erat. Sed tincidunt bibendum sollicitudin.</p>
<div class="abs news-rule" style="top:722px"></div>

<h3 class="abs news-title" style="top:730px">Phasellus in nunc purus <span>JUNE 28, 2013</span></h3>
<div class="abs news-thumb" style="top:753px" role="img" aria-label="Interior room thumbnail"></div>
<p class="abs news-copy" style="top:754px">Morbi vel metus vitae mi aliquam interdu sed eleifend quam. Sed sed ultrices erat. Sed tincidunt bibendum sollicitudin.</p>
<div class="abs news-rule" style="top:808px"></div>

<h2 class="abs section-title" style="left:677px;top:819px">NEWSLETTER SIGN UP</h2>
<p class="abs news-copy" style="left:677px;top:845px;width:230px">Stay up to date with latest news from our company. We promise we won't spam you.</p>
<div class="abs field" style="top:881px">Your Name...</div>
<div class="abs field" style="top:919px">Your Name...</div>
<div class="abs" style="left:677px;top:956px">
  <svg width="109" height="30" viewBox="0 0 109 30" aria-hidden="true">
    <rect x=".5" y=".5" width="108" height="29" fill="#2c2c2c" stroke="#777"/>
    <polygon points="70,1 108,1 108,29 84,29" fill="var(--tan)"/>
    <polyline points="91,9 97,15 91,21" fill="none" stroke="#222" stroke-width="1.3"/>
  </svg>
  <span class="btn-label" style="left:16px;top:9px">SUBMIT</span>
</div>

<footer class="abs footer"></footer>
<h4 class="abs f-head" style="left:183px">SUPPORTS</h4>
<ul class="abs f-links" style="left:183px"><li>Portfolio</li><li class="on">Dorvel Rewards</li><li>News</li></ul>
<h4 class="abs f-head" style="left:382px">LEGAL INFO</h4>
<ul class="abs f-links" style="left:382px"><li>Terms Of Use</li><li>Privacy Policy</li><li>Copyright Policy</li></ul>
<h4 class="abs f-head" style="left:567px">MORE</h4>
<ul class="abs f-links" style="left:567px"><li>Get Start</li><li>Learn More</li><li>Log In</li></ul>
<h4 class="abs f-head" style="left:730px">CONTACT US</h4>
<div class="abs map" role="img" aria-label="Faint world map decoration"></div>
<div class="abs contact">
  <div style="top:0">
    <svg width="10" height="10" viewBox="0 0 10 10" aria-hidden="true"><polygon points="5,1 10,5.5 8.5,5.5 8.5,9 1.5,9 1.5,5.5 0,5.5" fill="var(--tan)"/></svg>
    <p>4180 NW Alder Ridge Rd, #12, Fernvale,<br>OR 97000</p>
  </div>
  <div style="top:31px">
    <svg width="10" height="10" viewBox="0 0 10 10" aria-hidden="true"><rect x="0" y="0" width="10" height="10" rx="2" fill="var(--tan)"/><path d="M3,2 L4.5,2 L5,4 L4,5 Q5,6.5 6,7 L7,6 L9,6.5 L9,8 Q5,8.5 2.5,5 Q2,3 3,2Z" fill="#2f2f2d"/></svg>
    <p>(555) 310-2846</p>
  </div>
  <div style="top:51px">
    <svg width="10" height="10" viewBox="0 0 10 10" aria-hidden="true"><rect x="0" y="2" width="10" height="6.5" fill="var(--tan)"/><polyline points="0,2 5,6 10,2" fill="none" stroke="#2f2f2d" stroke-width=".9"/></svg>
    <p>info@dorvelbuildworks.com</p>
  </div>
</div>

<div class="abs footer-bar">© 2010 <span>Dorvel</span> Buildworks</div>

</body>
</html>
```